Building company business card

Design and print business cards for BRENTHOLM PTY LTD.
A residantial homes building company.
Mark Lantern already designed the company Logo.

```html
<!DOCTYPE html>
<html lang="en">
<head>
<meta charset="utf-8">
<title>Brentholm Pty Ltd – Business Card</title>
<link href="https://fonts.googleapis.com/css2?family=Lato:ital,wght@0,400;0,700;0,900;1,700&display=swap" rel="stylesheet">
<style>
  :root {
    --backdrop: #151515;
    --card-blue: #0f1f7a;
    --card-blue-deep: #0b1766;
    --ink-white: #ffffff;
    --accent-gold: #e2b13c;
  }
  * { margin: 0; padding: 0; box-sizing: border-box; }
  html, body {
    width: 1200px; height: 963px; overflow: hidden;
    background: var(--backdrop);
    font-family: "Lato", sans-serif;
    color: var(--ink-white);
  }
  .business-card {
    position: absolute;
    left: 100px; top: 196px;
    width: 1000px; height: 571px;
    background: linear-gradient(135deg, var(--card-blue) 0%, var(--card-blue-deep) 100%);
    border-radius: 4px;
    overflow: hidden;
  }
  .brand {
    position: absolute; left: 70px; top: 90px;
    display: flex; align-items: center; gap: 14px;
  }
  .brand-mark {
    width: 34px; height: 34px; background: var(--accent-gold);
  }
  .brand-name {
    font-weight: 900; font-size: 52px; letter-spacing: 1px;
    color: var(--ink-white);
  }
  .company-block { position: absolute; left: 70px; top: 250px; width: 520px; }
  .company-name { font-weight: 700; font-style: italic; font-size: 22px; }
  .company-address { font-size: 21px; margin-top: 6px; }
  .divider { height: 2px; background: var(--ink-white); margin: 14px 0 16px; }
  .contact-row {
    display: flex; flex-wrap: wrap; gap: 10px 28px;
    font-size: 21px; align-items: center;
  }
  .contact-item { display: flex; align-items: center; gap: 10px; }
  .contact-item svg { width: 20px; height: 22px; flex: none; }
  .person { position: absolute; right: 80px; top: 260px; text-align: right; }
  .person-name { font-weight: 900; font-size: 28px; letter-spacing: 0.5px; }
  .person-role { font-size: 22px; margin-top: 4px; }
  .gold-tab {
    position: absolute; right: 0; top: 400px;
    width: 16px; height: 60px; background: var(--accent-gold);
    border-radius: 4px 0 0 4px;
  }
</style>
</head>
<body>
  <section class="business-card">
    <div class="brand">
      <span class="brand-mark"></span>
      <span class="brand-name">BRENTHOLM</span>
    </div>

    <div class="company-block">
      <p class="company-name">Brentholm Pty Ltd</p>
      <p class="company-address">Unit 14, Po Box 208, Ferncliff North, Vic 3199</p>
      <div class="divider"></div>
      <div class="contact-row">
        <span class="contact-item">
          <svg viewBox="0 0 20 22" fill="none" stroke="#fff" stroke-width="2"><rect x="5" y="1" width="10" height="20" rx="2"/><line x1="9" y1="17" x2="11" y2="17"/></svg>
          0400 318 527
        </span>
        <span class="contact-item">
          <svg viewBox="0 0 20 22" fill="none" stroke="#fff" stroke-width="2"><rect x="5" y="1" width="10" height="20" rx="2"/><line x1="9" y1="17" x2="11" y2="17"/></svg>
          0400 642 913
        </span>
        <span class="contact-item">
          <svg viewBox="0 0 20 22" fill="none" stroke="#fff" stroke-width="2"><rect x="1" y="5" width="18" height="12"/><polyline points="1,5 10,12 19,5"/></svg>
          dc@brentholm-pl.com
        </span>
      </div>
    </div>

    <div class="person">
      <p class="person-name">DORIAN (Dee) CALLOWAY</p>
      <p class="person-role">Director</p>
    </div>

    <span class="gold-tab"></span>
  </section>
</body>
</html>
```